Book Cover Design Book About Commercial Real Estate Investing

I need a book cover designed for my upcoming book.
Need cover for paperback and hardcover book.

The Book is about investing in net lease commercial property.

The book title:

The Steady Yield Manual
Proven Methods For Passive Landlord Buyers
By Mara Colby

Should be minimalist, clean, authoritative, convey money, trust, & growth
I think I like the colors white red and black.
I want a front cover at this time.

Samples I like are included. - the red white and blacks are my favorites

My company is The Corlane Circle
you can learn more about Triple Net Properties at my website
www.TheCorlaneCircle.com

the symbol NNN = Triple net in commercial real estate

Target Market(s)

Affluent male conservative investors

Industry/Entity Type

Real Estate

Requirements
Nice to have
• Sports Motif - - diagrams of sports plays from playbook
• google - Diagrams of sports plays -

```html
<!DOCTYPE html>
<html lang="en">
<head>
<meta charset="utf-8">
<title>The Steady Yield Manual — Book Cover Wrap</title>
<link rel="stylesheet" href="https://fonts.googleapis.com/css2?family=Bebas+Neue&family=Open+Sans:ital,wght@1,400&display=swap">
<style>
  :root {
    --cover-red: #ee2b2a;
    --coin-red: #f0513f;
    --band-black: #000000;
    --paper-white: #ffffff;
    --rule-white: rgba(255, 255, 255, 0.75);
    --spine-line: rgba(255, 255, 255, 0.35);
    --brand-green: #4caf32;
  }
  * { box-sizing: border-box; margin: 0; padding: 0; }
  html, body { width: 1200px; height: 733px; overflow: hidden; background: var(--band-black); }
  .wrap {
    position: relative; width: 1200px; height: 733px; overflow: hidden;
    background: var(--band-black);
    font-family: "Bebas Neue", "Arial Narrow", sans-serif;
    color: var(--paper-white);
  }
  .red-field {
    position: absolute; left: 0; top: 24px; width: 1200px; height: 593px;
    background: var(--cover-red);
  }
  .spine-edge {
    position: absolute; top: 24px; width: 1px; height: 593px; background: var(--spine-line);
  }
  .spine-edge--left { left: 557px; }
  .spine-edge--right { left: 647px; }

  /* back cover */
  .back-art {
    position: absolute; left: 168px; top: 240px; width: 225px; height: 150px;
    background: radial-gradient(ellipse at center, var(--coin-red) 0%, var(--cover-red) 75%);
    border-radius: 12px;
  }
  .back-tagline {
    position: absolute; left: 0; width: 557px; top: 420px; text-align: center;
    font-family: "Open Sans", Arial, sans-serif; font-style: italic; font-size: 19px;
  }

  /* front cover */
  .front { position: absolute; left: 647px; top: 0; width: 553px; height: 733px; }
  .title { position: absolute; left: 0; right: 0; top: 98px; text-align: center; line-height: 1; }
  .title__lead { display: block; font-size: 34px; letter-spacing: 1px; }
  .title__main { display: block; font-size: 212px; line-height: 0.8; letter-spacing: 1px; margin-top: 4px; }
  .title__tail { display: block; font-size: 31px; letter-spacing: 9px; margin-top: 6px; padding-left: 9px; }
  .subtitle {
    position: absolute; left: 110px; width: 364px; top: 376px; height: 43px;
    border-top: 1px solid var(--rule-white); border-bottom: 1px solid var(--rule-white);
    display: flex; align-items: center; justify-content: center;
    font-family: "Open Sans", Arial, sans-serif; font-style: italic; font-size: 18px; white-space: nowrap;
  }
  .author { position: absolute; left: 0; right: 0; top: 580px; text-align: center; font-size: 22px; letter-spacing: 0.5px; }
  .imprint {
    position: absolute; left: 0; right: 0; top: 662px;
    display: flex; align-items: center; justify-content: center; gap: 8px;
    font-size: 25px; letter-spacing: 0.5px;
  }
  .imprint__mark { width: 16px; height: 16px; background: var(--brand-green); }

  /* spine */
  .spine-author {
    position: absolute; left: 593px; top: 384px; writing-mode: vertical-rl;
    font-size: 18px; line-height: 1; white-space: nowrap;
  }
  .spine-title {
    position: absolute; left: 600px; top: 546px;
    transform: translate(-50%, -50%) rotate(90deg);
    display: flex; flex-direction: column-reverse; align-items: center;
    line-height: 1; white-space: nowrap;
  }
  .spine-title__lead { font-size: 11px; letter-spacing: 0.5px; }
  .spine-title__main { font-size: 50px; line-height: 0.82; }
  .spine-title__tail { font-size: 9px; letter-spacing: 2px; padding-left: 2px; }
  .spine-imprint {
    position: absolute; left: 603px; top: 670px; transform: translate(-50%, -50%) rotate(-90deg);
    display: flex; align-items: center; gap: 4px; white-space: nowrap; font-size: 13px; line-height: 1;
  }
  .spine-imprint .imprint__mark { width: 10px; height: 10px; }
</style>
</head>
<body>
<main class="wrap">
  <div class="red-field"></div>
  <div class="spine-edge spine-edge--left"></div>
  <div class="spine-edge spine-edge--right"></div>

  <section class="back">
    <div class="back-art" role="img" aria-label="Faint stacks of dollar coins"></div>
    <p class="back-tagline">Triple net in commercial real estate</p>
  </section>

  <section class="spine">
    <p class="spine-author">BY MARA COLBY</p>
    <h2 class="spine-title">
      <span class="spine-title__lead">THE STEADY</span>
      <span class="spine-title__main">YIELD</span>
      <span class="spine-title__tail">MANUAL</span>
    </h2>
    <p class="spine-imprint"><span class="imprint__mark"></span>THE CORLANE CIRCLE</p>
  </section>

  <section class="front">
    <h1 class="title">
      <span class="title__lead">THE STEADY</span>
      <span class="title__main">YIELD</span>
      <span class="title__tail">MANUAL</span>
    </h1>
    <p class="subtitle">Proven Methods For Passive Landlord Buyers</p>
    <p class="author">BY MARA COLBY</p>
    <p class="imprint"><span class="imprint__mark"></span>THE CORLANE CIRCLE</p>
  </section>
</main>
</body>
</html>
```